ATM Website-Great Opportunity for Portability

Hey We need YOU to help us make our ATM (Automatic Teller Machine)Website!!) We are a million dollar business that will look great on your portfolio! Our Name is "CORNER CASH POINT"
Previous ATM business (now sold) was www.cashbrivo.com.au (site being pulled down so look at it fast!)
The winner will get the same package that we will giving to the winner of our other project! (worth over $9,000)
http://jobs.pixelvorn.com/job.aspx?id=4827
**we are making a series of sites/applications Winners will be solo invited to work on all upcoming projects of that catigory**
***we are also looking for Outstanding freelance guys to work with on all future projects***
Main Points!!
1: one main page (that is not a blog!)
2: Then the Theme!
3: I don't want it to look like a word-press
I.e like this guys Word press http://www.trasqueld.com/
See how he has one main page then the rest are WP Theme :)
Key points to the Home Page!
See attached pic for the menu's needed and the call now key.
Main page needs to have
1. Clean, uncluttered, and follow the feel of our LOGO (attached) Be creative but simplistic with the page. Round curves are good)
2. Large hero images of happy poeple in the community but not looking too stocky or contrived - natural smiles, natural expressions, With Image of OUR ATM on the page!
3. Easy navigation
4: (3 big buttons like on our competitors site
(http://www.brightfundpoint.com.au/) With the titles
(get an ATM (and beside it "for your business")
(Own an ATM (increase your investment Portfolio)
(Latest ATM (See an ATM in action)
For the Theme Page,
It must flow on from the main menu but have a bread crum trail on the page of all the sub links somewhere on the left of the page (or somewhere else that might look better.
Theme page should have a Call now or email now option!! If you can fit in 2 without it looking cluttered that would be good.
I will attach our brochures so you can get a feel of our product.
Also you should be able to extract images from our brochure using GLEMBRA DOC TOOL or similar PDF editor if needed!!
logo attached and also found at www.cornercashpoint.com.au
Good Fonts to use!
Helvetica Neue LT (bold thin ect)
Helvetica Neue LT Com
Target Market(s)
Business Owners and Investors
Industry/Entity Type
Investment
Requirements
Must have
- The Call now Features in the attached file, Clean layout
Should not have
- Should not look like stock photo's and a cheap website or a template...

```html
<!DOCTYPE html>
<html lang="en">
<head>
<meta charset="utf-8">
<title>Corner Cash Point – Reasons why I need an ATM</title>
<link href="https://fonts.googleapis.com/css2?family=Arimo:wght@400;700&display=swap" rel="stylesheet">
<style>
  :root {
    --green: #6cb52d;
    --green-dark: #3f8f1a;
    --green-text: #3c7d14;
    --green-light: #d9ecb8;
    --grey: #9c9c9c;
    --white: #ffffff;
    --shadow: rgba(0,0,0,0.18);
  }
  * { margin: 0; padding: 0; box-sizing: border-box; }
  html, body { width: 1200px; height: 900px; overflow: hidden; }
  body {
    position: relative;
    font-family: "Arimo", Arial, sans-serif;
    background: linear-gradient(180deg, #f2f8e8 0%, #e3f0cc 45%, #c6e08f 100%);
  }
  .brand {
    position: absolute; left: 130px; top: 36px;
    display: flex; align-items: center; gap: 22px;
  }
  .brand-dot {
    width: 104px; height: 104px; border-radius: 50%;
    background: var(--green);
  }
  .brand-name {
    font-size: 50px; font-weight: 400; color: var(--grey); white-space: nowrap;
  }
  .main-nav {
    position: absolute; left: 59px; top: 144px; width: 800px; height: 66px;
  }
  .main-nav svg { position: absolute; inset: 0; }
  .main-nav ul { list-style: none; position: absolute; inset: 0; }
  .main-nav li {
    position: absolute; top: 31px; font-size: 14px; color: var(--green-text); white-space: nowrap;
  }
  .main-panel {
    position: absolute; left: 90px; top: 244px; width: 1023px; height: 574px;
    background: var(--white); border: 2px solid var(--green-light);
    border-radius: 22px; box-shadow: 0 4px 10px var(--shadow);
  }
  .side-tab {
    position: absolute; left: 832px; top: 244px; width: 332px; height: 76px;
  }
  .content-panel {
    position: absolute; left: 164px; top: 267px; width: 875px; height: 430px;
    background: linear-gradient(180deg, #f7f7f7, #ececec);
    border-left: 3px solid var(--green); border-right: 3px solid var(--green);
    border-top: 3px solid var(--green);
    border-radius: 18px 18px 0 0;
  }
  .shelf {
    position: absolute; left: 98px; top: 690px; width: 1010px; height: 58px;
    background: linear-gradient(180deg, #e2e2e2, #fdfdfd 55%, #ececec);
    border-radius: 0 0 30px 30px; box-shadow: 0 8px 12px rgba(0,0,0,0.08);
  }
  .reasons { position: absolute; left: 273px; top: 290px; }
  .reasons h1 {
    font-size: 26px; font-weight: 700; color: var(--green); margin-bottom: 9px; white-space: nowrap;
  }
  .reasons ul { list-style: none; }
  .reasons li {
    position: relative; padding-left: 18px; font-size: 14.5px; line-height: 17px;
    color: var(--green-text); margin-bottom: 9px; max-width: 480px;
  }
  .reasons li::before {
    content: ""; position: absolute; left: 2px; top: 5px;
    width: 9px; height: 9px; border-radius: 50%;
    background: radial-gradient(circle at 35% 35%, #a6d86b, var(--green-dark));
  }
  .reasons li.narrow { max-width: 320px; }
  .atm-tall {
    position: absolute; left: 912px; top: 29px; width: 152px; height: 270px;
    background: linear-gradient(90deg, #8a9a80, #4aa52a 40%, #2f8a1c);
    border-radius: 14px 28px 6px 6px;
  }
  .atm-small {
    position: absolute; left: 176px; top: 559px; width: 84px; height: 152px;
    background: linear-gradient(90deg, #3f9c22, #62b735 50%, #9aa39a);
    border-radius: 8px 14px 4px 4px;
  }
  .crowd-photo {
    position: absolute; left: 604px; top: 514px; width: 427px; height: 183px;
    background: linear-gradient(180deg, rgba(240,240,240,0), #c9ccd3 30%, #6f7890);
    border-radius: 6px;
  }
  .call-bar {
    position: absolute; left: 223px; top: 787px; width: 750px; height: 53px;
    border-radius: 12px; border: 2px solid var(--green-light);
    background: linear-gradient(180deg, #8ccc4f, var(--green-dark));
    box-shadow: 0 3px 6px var(--shadow);
    display: flex; align-items: center; overflow: hidden; white-space: nowrap;
  }
  .call-label {
    flex: 0 0 auto; height: 100%; width: 268px; background: var(--white);
    border-radius: 10px 28px 28px 10px;
    display: flex; align-items: center; padding-left: 18px;
    font-size: 19px; font-weight: 700; color: var(--green-text);
  }
  .call-phone {
    flex: 0 0 auto; margin-left: 18px; font-size: 25px; font-weight: 700; color: var(--white);
  }
  .call-email {
    flex: 0 0 auto; margin-left: 14px; font-size: 17px; font-weight: 700; color: var(--white);
  }
</style>
</head>
<body>
  <header class="brand">
    <span class="brand-dot"></span>
    <span class="brand-name">CORNER CASH POINT</span>
  </header>

  <div class="main-panel"></div>

  <svg class="side-tab" viewBox="0 0 332 76">
    <defs>
      <linearGradient id="tabFill" x1="0" y1="0" x2="0" y2="1">
        <stop offset="0" stop-color="#ffffff"/>
        <stop offset="1" stop-color="#e2e2e2"/>
      </linearGradient>
    </defs>
    <path d="M0 2 H290 Q330 2 330 40 Q330 74 296 74 H14 Q0 74 0 60 Z" fill="url(#tabFill)"/>
    <path d="M0 74 H330" stroke="#6cb52d" stroke-width="3"/>
  </svg>

  <div class="content-panel"></div>
  <div class="shelf"></div>

  <nav class="main-nav">
    <svg viewBox="0 0 800 66" preserveAspectRatio="none">
      <defs>
        <linearGradient id="navFill" x1="0" y1="0" x2="0" y2="1">
          <stop offset="0" stop-color="#ffffff"/>
          <stop offset="0.6" stop-color="#f1f1f1"/>
          <stop offset="1" stop-color="#d6d6d6"/>
        </linearGradient>
      </defs>
      <path d="M0 64 V26 Q0 4 24 4 H720 Q760 4 790 40 Q780 64 740 64 Z" fill="url(#navFill)"/>
      <path d="M0 64 H760" stroke="#6cb52d" stroke-width="3"/>
      <g stroke="#cfcfcf" stroke-width="1.5" fill="none">
        <path d="M72 62 Q62 30 82 6"/>
        <path d="M210 62 Q200 30 220 6"/>
        <path d="M371 62 Q361 30 381 6"/>
        <path d="M467 62 Q457 30 477 6"/>
        <path d="M520 62 Q510 30 530 6"/>
        <path d="M629 62 Q619 30 639 6"/>
        <path d="M691 62 Q681 30 701 6"/>
      </g>
    </svg>
    <ul>
      <li style="left:22px">Home</li>
      <li style="left:84px">Why I need a ATM</li>
      <li style="left:221px">Product and Services</li>
      <li style="left:383px">Testimonial</li>
      <li style="left:480px">F&amp;Q</li>
      <li style="left:528px">Invest with us</li>
      <li style="left:638px">About</li>
      <li style="left:707px">Contact</li>
    </ul>
  </nav>

  <div class="atm-tall" role="img" aria-label="Green branded ATM machine standing upright"></div>

  <section class="reasons">
    <h1>Reasons why I need an ATM</h1>
    <ul>
      <li>The ATM is FREE and so is installation and de-installation!</li>
      <li>Pay your ren/loan with the BONUS INCOME you get from withdrawals</li>
      <li>Never pay EFTPOS charge again</li>
      <li>People are fighting against the banks making all the profits!</li>
      <li>24 hour support and local maintenance team</li>
      <li>Increase staff productivity by saving time on EFTPOS</li>
      <li>Increase retail sales by 8% to 14% on average just by having an ATM</li>
      <li>Attract more customers by having a safe ATM</li>
      <li class="narrow">Saves trips to the bank by filling your ATM with your time</li>
      <li class="narrow">Secure customers instead of sending them to your competitors to get cash</li>
      <li class="narrow">Your ATM provides extra security as it has built-in camera and safe.</li>
    </ul>
  </section>

  <div class="atm-small" role="img" aria-label="Small green branded ATM machine"></div>
  <div class="crowd-photo" role="img" aria-label="Row of happy people cheering with raised arms"></div>

  <footer class="call-bar">
    <span class="call-label">For more info please call</span>
    <span class="call-phone">1800 442 918</span>
    <span class="call-email">info@cornercashpoint.com.au</span>
  </footer>
</body>
</html>
```